Financial Services Business Card Design

We are a financial services company Based in London, offering Short term Funding Solutions for companies, raising anywhere between £20,000 and £25million pounds.

The Card must have a professional look as it is going to be handed out to professionals I.E Solicitors, Accountants, Company directors and Business owners.

See Attached our company Logo

Industry/Entity Type

Business

Contact Information for Business Card

Lewis Thorncroft
Suite 41
R K House
Bramblecote Lane
Ashmere
HP19 4QX

```html
<!DOCTYPE html>
<html lang="en">
<head>
<meta charset="utf-8">
<title>Meridale Capital – Business Card</title>
<link href="https://fonts.googleapis.com/css2?family=Open+Sans:wght@400;700&display=swap" rel="stylesheet">
<style>
  :root {
    --backdrop: #e9e7e4;
    --card: #2e2e2e;
    --brand-blue: #2f7bc8;
    --text-light: #e4e4e4;
    --text-white: #ffffff;
  }
  * { margin: 0; padding: 0; box-sizing: border-box; }
  html, body {
    width: 1200px;
    height: 1000px;
    overflow: hidden;
    background: var(--backdrop);
    font-family: "Open Sans", Arial, sans-serif;
  }
  .canvas {
    position: relative;
    width: 1200px;
    height: 1000px;
  }
  .card {
    position: absolute;
    left: 287px;
    width: 626px;
    height: 364px;
    background: var(--card);
    box-shadow: 0 2px 6px rgba(0,0,0,0.25);
  }
  .card-front { top: 123px; }
  .card-back { top: 511px; }

  .brand {
    position: absolute;
    left: 0;
    right: 0;
    top: 208px;
    display: flex;
    align-items: center;
    justify-content: center;
    gap: 14px;
  }
  .brand-mark {
    width: 24px;
    height: 24px;
    background: var(--brand-blue);
  }
  .brand-name {
    color: var(--brand-blue);
    font-weight: 700;
    font-size: 34px;
    letter-spacing: 0.5px;
  }

  .contact {
    position: absolute;
    right: 20px;
    top: 124px;
    text-align: right;
    color: var(--text-light);
    font-size: 14px;
    line-height: 20px;
  }
  .contact-name {
    color: var(--text-white);
    font-weight: 700;
    font-size: 15px;
    line-height: 23px;
    margin-right: 8px;
  }
  .contact-role {
    color: var(--text-white);
    font-size: 15px;
    line-height: 23px;
    margin-right: 8px;
    margin-bottom: 24px;
  }
  .contact-address { margin-bottom: 5px; }
  .contact-phones { margin-bottom: 5px; }
</style>
</head>
<body>
<main class="canvas">
  <section class="card card-front">
    <div class="brand">
      <span class="brand-mark"></span>
      <span class="brand-name">Meridale Capital</span>
    </div>
  </section>

  <section class="card card-back">
    <div class="contact">
      <p class="contact-name">Lewis Thorncroft</p>
      <p class="contact-role">Director</p>
      <div class="contact-address">
        <p>Suite 41, R K House</p>
        <p>Bramblecote Lane</p>
        <p>Ashmere, HP19 4QX</p>
      </div>
      <div class="contact-phones">
        <p>M: 07700 914263</p>
        <p>T : 0800 612 4407</p>
      </div>
      <div class="contact-online">
        <p>E: lewis@meridalecap.co.uk</p>
        <p>W: www.meridalecap.co.uk</p>
      </div>
    </div>
  </section>
</main>
</body>
</html>
```